political campaign lawn sign - Governor's Council in Massachuesetts

We are looking for a political lawn sign. We are running a campaign for Governor's Council in Massachusetts. This sign will be on the lawn of homes and businesses so people driving by will see it. It needs to be simple and bold. The last name is long so maybe it could say vote for Marty and then Kolbeck will be big a bold on the next line??
We need it to say:
Vote for Martin Kolbeck
Governor's Council.

Target Market(s)

local residents

Industry/Entity Type

Politcal Campaign

Font styles to use
Sans Serif
Other font styles liked:
• not sure what font but a modern looking one such as Helvetica, Arial, Sans Seri, sharp sans..

Colors
0054AA
0677BA
7BADD7
CADEEF
E8F1F8
00AB8E
00BBA5
67D7C9
C6EFE9
E9F9F6
FFF300
FFF600
FEFA6F
FFFEC7
FFFEE8

Requirements
Must have
• My name written out with a Capital D and R but lower case for every other letter so its Marty Kolbeck
Nice to have
• modern font , the Colors of the lawn sign should have Blue, Yellow and White something bold that will stand out
Should not have
• any maps of Massachusetts

```html
<!DOCTYPE html>
<html lang="en">
<head>
<meta charset="utf-8">
<title>Vote for Marty Kolbeck – Governor's Council</title>
<link rel="stylesheet" href="https://fonts.googleapis.com/css2?family=Bebas+Neue&family=Oswald:wght@600&display=swap">
<style>
  :root {
    --navy: #1d2b5c;
    --gold: #e8b02e;
    --white: #ffffff;
    --backdrop: #eceeec;
  }
  html, body {
    margin: 0;
    padding: 0;
    width: 1200px;
    height: 1118px;
    overflow: hidden;
    background: var(--backdrop);
  }
  .lawn-sign {
    position: absolute;
    left: 20px;
    top: 124px;
    width: 1160px;
    height: 870px;
    display: block;
  }
  .sign-headline { font-family: "Bebas Neue", "Oswald", sans-serif; }
  .sign-connector { font-family: "Oswald", sans-serif; font-weight: 600; }
  .fill-navy { fill: var(--navy); }
  .fill-gold { fill: var(--gold); }
  .fill-white { fill: var(--white); }
</style>
</head>
<body>
<svg class="lawn-sign" viewBox="0 0 1240 930" role="img" aria-label="Vote for Marty Kolbeck, Governor's Council">
  <!-- sign panels -->
  <rect class="panel-white fill-white" x="0" y="0" width="1240" height="930"/>
  <rect class="panel-navy fill-navy" x="0" y="38" width="1240" height="720"/>
  <rect class="top-band fill-gold" x="0" y="0" width="1240" height="38"/>
  <polygon class="vote-tab fill-gold" points="327,37 914,37 855,224 385,224"/>

  <!-- pointer arrows -->
  <g class="pointers-left fill-gold">
    <polygon points="87,129 114,144 87,159"/>
    <polygon points="137,129 164,144 137,159"/>
    <polygon points="186,129 213,144 186,159"/>
    <polygon points="235,129 262,144 235,159"/>
  </g>
  <g class="pointers-right fill-gold">
    <polygon points="1005,129 978,144 1005,159"/>
    <polygon points="1054,129 1027,144 1054,159"/>
    <polygon points="1104,129 1077,144 1104,159"/>
    <polygon points="1155,129 1128,144 1155,159"/>
  </g>

  <!-- messaging -->
  <text class="sign-headline call-to-action fill-white" x="620" y="194" font-size="210" text-anchor="middle">VOTE</text>

  <text class="first-name-line" x="620" y="472" text-anchor="middle">
    <tspan class="sign-connector fill-white" font-size="96">for</tspan>
    <tspan class="sign-headline fill-gold" font-size="293" dx="18">MARTY</tspan>
  </text>

  <text class="sign-headline last-name fill-gold" x="620" y="708" font-size="293" text-anchor="middle">KOLBECK</text>

  <text class="sign-headline office-title fill-navy" x="620" y="892" font-size="150" text-anchor="middle">GOVERNOR'S COUNCIL</text>
</svg>
</body>
</html>
```